Business Card design for new private practice opening

I need a business card design for my new private practice with my new logo uploaded as a file
On the front the logo
On the back: maybe a small logo somewhere?
Priv. Doz. DDr. Corinna Vestaluk
Fachärztin für Allgemein- & Viszeralchirurgie
Address: xxx
Tel: xxx
Mobil:xxx
Webseite:xxx
Email:xxx

Contact Information for Business Card

See project description above for details

Requirements
Nice to have
• I would like the colors of the logo incorporated into the business card

```html
<!DOCTYPE html>
<html lang="de">
<head>
<meta charset="utf-8">
<title>Vestaluk Chirurgie – Visitenkarte</title>
<link rel="stylesheet" href="https://fonts.googleapis.com/css2?family=Poppins:wght@400;500;600&display=swap">
<style>
  :root {
    --teal: #45b9b5;
    --grey: #8c8c8c;
    --grey-dark: #7a7a7a;
    --paper: #ffffff;
    --stage: #2b2b2b;
  }
  * { box-sizing: border-box; margin: 0; padding: 0; }
  html, body { width: 1200px; height: 1200px; overflow: hidden; }
  body {
    background: var(--stage);
    font-family: "Poppins", sans-serif;
    display: flex;
    flex-direction: column;
    align-items: center;
    justify-content: center;
    gap: 40px;
  }
  .card {
    position: relative;
    width: 960px;
    height: 540px;
    background: var(--paper);
    overflow: hidden;
  }

  /* Front */
  .card-front {
    display: flex;
    flex-direction: column;
    align-items: center;
    justify-content: center;
  }
  .brand {
    display: flex;
    align-items: center;
    gap: 36px;
  }
  .brand-mark {
    width: 150px;
    height: 150px;
    border: 7px solid var(--grey);
    border-radius: 50%;
  }
  .brand-name {
    color: var(--grey);
    font-weight: 600;
    font-size: 58px;
    line-height: 1.05;
    letter-spacing: 3px;
    text-transform: uppercase;
  }
  .front-web {
    margin-top: 44px;
    color: var(--teal);
    font-size: 20px;
    letter-spacing: 6px;
  }

  /* Back */
  .back-art { position: absolute; inset: 0; }
  .contact {
    position: absolute;
    left: 44px;
    top: 150px;
    color: var(--grey-dark);
  }
  .contact-name {
    color: var(--teal);
    font-weight: 600;
    font-size: 30px;
    line-height: 1.2;
  }
  .contact-title {
    font-size: 18px;
    margin-bottom: 16px;
  }
  .contact-address {
    font-size: 20px;
    line-height: 1.3;
    margin-bottom: 14px;
  }
  .contact-list { list-style: none; font-size: 20px; line-height: 1.5; }
  .contact-list li { display: flex; align-items: center; gap: 12px; }
  .contact-icon { width: 22px; height: 22px; flex: none; }
</style>
</head>
<body>

  <section class="card card-front">
    <div class="brand">
      <div class="brand-mark"></div>
      <h1 class="brand-name">Vestaluk<br>Chirurgie</h1>
    </div>
    <p class="front-web">www.vestaluk-praxis.at</p>
  </section>

  <section class="card card-back">
    <svg class="back-art" viewBox="0 0 960 540" width="960" height="540" aria-hidden="true">
      <rect width="960" height="540" fill="var(--teal)"/>
      <ellipse cx="200" cy="280" rx="640" ry="360" fill="var(--paper)"/>
      <ellipse cx="200" cy="290" rx="615" ry="340" fill="none" stroke="var(--grey)" stroke-width="9"/>
      <circle cx="792" cy="215" r="72" fill="var(--paper)" stroke="var(--grey)" stroke-width="7"/>
    </svg>

    <div class="contact">
      <h2 class="contact-name">Priv. Doz. DDr. Corinna Vestaluk</h2>
      <p class="contact-title">Fachärztin für Allgemein- &amp; Viszeralchirurgie</p>
      <p class="contact-address">Postfach 47 Lindenweg 12<br>8010 Graz, Austria</p>
      <ul class="contact-list">
        <li>
          <svg class="contact-icon" viewBox="0 0 22 22"><circle cx="11" cy="11" r="11" fill="var(--teal)"/><path d="M8 6h2l1 3-1.5 1a6 6 0 0 0 2.5 2.5L13 11l3 1v2a2 2 0 0 1-2 1A8 8 0 0 1 7 8a2 2 0 0 1 1-2z" fill="#fff"/></svg>
          555-014-2236
        </li>
        <li>
          <svg class="contact-icon" viewBox="0 0 22 22"><circle cx="11" cy="11" r="11" fill="var(--teal)"/><rect x="7.5" y="5" width="7" height="12" rx="1.5" fill="none" stroke="#fff" stroke-width="1.6"/></svg>
          555-014-2237
        </li>
        <li>
          <svg class="contact-icon" viewBox="0 0 22 22"><circle cx="11" cy="11" r="11" fill="var(--teal)"/><rect x="5" y="7" width="12" height="8" fill="none" stroke="#fff" stroke-width="1.5"/><path d="M5 7l6 5 6-5" fill="none" stroke="#fff" stroke-width="1.5"/></svg>
          info@vestaluk-praxis.at
        </li>
        <li>
          <svg class="contact-icon" viewBox="0 0 22 22"><circle cx="11" cy="11" r="11" fill="var(--teal)"/><circle cx="11" cy="11" r="6" fill="none" stroke="#fff" stroke-width="1.3"/><path d="M5 11h12M11 5c-3 3-3 9 0 12M11 5c3 3 3 9 0 12" fill="none" stroke="#fff" stroke-width="1.1"/></svg>
          www.vestaluk-praxis.at
        </li>
      </ul>
    </div>
  </section>

</body>
</html>
```